Data Visualization (graphs, tables, models, circles)

We need an intuitive - user friendly - and fresh design line for our data visualization.

You know. Keep The Page Calm!

Our core product is based on the presentation and interpretation of different data sources that we combine into graphs, tables, charts etc and make visible to clients through a web platform and or Reports. Our business area is Search & Social Media Intelligence.

See Vantrel.com for some inspiration in terms of current colors and a better understanding of the company. Our Logo / Name is the only one thing that cannot be changed. Everything else is up to you. Feel free to ask questions.

I have attached a few screenshots of some of our features and as you can see - there has never been a designer on this assignment. We are looking for a long term relationship with a designer that can work with us on an ongoing basis.

Design of graphs/models/circles/tables needs to be able to fit into Infographics also.

We are basically looking for an identity for our data visualization. Meaning that readers / target audience can recognize our graphs and say: Check out the cool graphs by Vantrel :-)

Think: Plorvex, TallyNorth, etc. in terms of data presentation.
Updates

Project Deadline Extended
Reason: Due to illness we lost a few days last week and have not have sufficient time to look through the different designs.

Target Market(s)

Marketing People, CEO's, Strategic Planners, Ad Agencies, Decision Makers

Industry/Entity Type

Business

Requirements
Must have
• Must present at least 1 line graph (like file 1 and 2), 1 pie chart, 1 column graph and 1 matrix (like file3).

```html
<!DOCTYPE html>
<html lang="en">
<head>
<meta charset="utf-8">
<title>SEO Deep Dive – 6 Years View</title>
<link href="https://fonts.googleapis.com/css2?family=Open+Sans:ital,wght@0,400;0,700;1,400&display=swap" rel="stylesheet">
<style>
  :root {
    --canvas: #ffffff;
    --paper: #ffffff;
    --ink: #000000;
    --label: #7a7a7a;
    --legend-text: #9a9a9a;
    --brand: #d2232a;
    --footer-band: #afafaf;
    --y2007: #bb2310;
    --y2008: #ffa683;
    --y2009: #ffd681;
    --y2010: #9ad27b;
    --y2011: #78c6d9;
    --y2012: #a69a90;
    --y2007-side: #6a160a;
    --y2008-side: #855644;
    --y2009-side: #857045;
    --y2010-side: #4c6a3c;
    --y2011-side: #3a6070;
    --y2012-side: #6e625a;
  }
  html, body {
    margin: 0;
    padding: 0;
    width: 1200px;
    height: 1000px;
    overflow: hidden;
    background: var(--canvas);
    font-family: "Open Sans", Arial, sans-serif;
  }
  .slide {
    position: relative;
    width: 1200px;
    height: 1000px;
  }
  .slide-art {
    position: absolute;
    left: 0;
    top: 0;
  }
  .header-title {
    position: absolute;
    left: 117px;
    top: 117px;
    margin: 0;
    font-size: 37px;
    font-weight: 400;
    color: #fff;
    line-height: 1.1;
  }
  .header-title strong { font-weight: 700; }
  .header-subtitle {
    position: absolute;
    left: 615px;
    top: 127px;
    margin: 0;
    font-size: 22px;
    font-weight: 400;
    color: #fff;
  }
  .brand-name {
    position: absolute;
    left: 1046px;
    top: 200px;
    font-size: 24px;
    font-weight: 700;
    color: var(--brand);
    letter-spacing: -0.5px;
  }
  .legend {
    position: absolute;
    left: 931px;
    top: 450px;
    margin: 0;
    padding: 0;
    list-style: none;
  }
  .legend-item {
    display: flex;
    align-items: center;
    height: 46px;
    font-size: 21px;
    color: var(--legend-text);
  }
  .legend-swatch {
    width: 22px;
    height: 22px;
    border-radius: 50%;
    margin-right: 17px;
  }
  .pie-label {
    font-family: "Open Sans", Arial, sans-serif;
    font-size: 20px;
    fill: var(--label);
  }
  .leader {
    fill: none;
    stroke-width: 3;
    stroke-linecap: round;
  }
  .footer-note {
    position: absolute;
    left: 63px;
    top: 866px;
    width: 1079px;
    height: 35px;
    line-height: 35px;
    margin: 0;
    text-align: center;
    font-size: 18px;
    font-style: italic;
    color: #fff;
    background: var(--footer-band);
  }
</style>
</head>
<body>
<main class="slide">
  <svg class="slide-art" width="1200" height="1000" viewBox="0 0 1200 1000" aria-hidden="true">
    <defs>
      <radialGradient id="floor-shadow">
        <stop offset="0" stop-color="#000" stop-opacity="0.16"/>
        <stop offset="1" stop-color="#000" stop-opacity="0"/>
      </radialGradient>
      <filter id="paper-shadow" x="-5%" y="-5%" width="110%" height="110%">
        <feDropShadow dx="0" dy="2" stdDeviation="2" flood-opacity="0.18"/>
      </filter>
    </defs>

    <!-- sheet -->
    <path d="M63 100 H1142 V794 L1088 848 H63 Z" fill="var(--paper)" filter="url(#paper-shadow)"/>
    <path d="M1088 848 L1142 794 L1098 806 Z" fill="#e4e4e4"/>

    <!-- header band -->
    <rect x="63" y="100" width="1079" height="81" fill="var(--ink)"/>
    <path d="M197 181 H236 L197 217 Z" fill="var(--ink)"/>

    <!-- floor shadow -->
    <ellipse cx="388" cy="783" rx="130" ry="22" fill="url(#floor-shadow)"/>

    <!-- pie chart -->
    <g class="pie" transform="translate(432 512)">
      <g class="pie-side">
        <g fill="var(--y2012-side)">
          <path transform="translate(-45 35)" d="M0 0 L-76.6 -162.9 A180 180 0 0 1 0 -180 Z"/>
        </g>
        <g fill="var(--y2011-side)">
          <path transform="translate(-45 35)" d="M0 0 L-145.6 -105.8 A180 180 0 0 1 -76.6 -162.9 Z"/>
          <path d="M-145.6 -105.8 A180 180 0 0 1 -110.6 -142 L-155.6 -107 A180 180 0 0 0 -190.6 -70.8 Z"/>
        </g>
        <g fill="var(--y2010-side)">
          <path transform="translate(-45 35)" d="M0 0 L-180 0 A180 180 0 0 1 -145.6 -105.8 Z"/>
          <path d="M-180 0 A180 180 0 0 1 -145.6 -105.8 L-190.6 -70.8 A180 180 0 0 0 -225 35 Z"/>
        </g>
        <g fill="var(--y2009-side)">
          <path transform="translate(-45 35)" d="M0 0 L-138.7 114.7 A180 180 0 0 1 -180 0 Z"/>
          <path d="M-138.7 114.7 A180 180 0 0 1 -180 0 L-225 35 A180 180 0 0 0 -183.7 149.7 Z"/>
        </g>
        <g fill="var(--y2008-side)">
          <path transform="translate(-45 35)" d="M0 0 L145.6 105.8 A180 180 0 0 1 -138.7 114.7 Z"/>
          <path d="M110.6 142 A180 180 0 0 1 -138.7 114.7 L-183.7 149.7 A180 180 0 0 0 65.6 177 Z"/>
        </g>
      </g>
      <g class="pie-top">
        <path d="M0 0 L145.6 105.8 A180 180 0 0 1 -138.7 114.7 Z" fill="var(--y2008)"/>
        <path d="M0 0 L-138.7 114.7 A180 180 0 0 1 -180 0 Z" fill="var(--y2009)"/>
        <path d="M0 0 L-180 0 A180 180 0 0 1 -145.6 -105.8 Z" fill="var(--y2010)"/>
        <path d="M0 0 L-145.6 -105.8 A180 180 0 0 1 -76.6 -162.9 Z" fill="var(--y2011)"/>
        <path d="M0 0 L-76.6 -162.9 A180 180 0 0 1 0 -180 Z" fill="var(--y2012)"/>
      </g>
      <g class="pie-lead-slice" transform="translate(40 -14)">
        <g fill="var(--y2007-side)">
          <path transform="translate(-40 30)" d="M0 0 L0 -180 A180 180 0 0 1 145.6 105.8 Z"/>
          <path d="M0 0 L0 -180 L-40 -150 L-40 30 Z"/>
          <path d="M0 0 L145.6 105.8 L105.6 135.8 L-40 30 Z"/>
        </g>
        <path d="M0 0 L0 -180 A180 180 0 0 1 145.6 105.8 Z" fill="var(--y2007)"/>
      </g>
    </g>

    <!-- leader lines -->
    <path class="leader" stroke="var(--y2007)" d="M548 350 C590 290 660 295 700 314 C718 323 730 328 742 325"/>
    <path class="leader" stroke="var(--y2008)" d="M548 665 C600 662 625 716 686 714"/>
    <path class="leader" stroke="var(--y2009)" d="M268 548 C212 540 192 592 147 580"/>
    <path class="leader" stroke="var(--y2010)" d="M252 470 C218 462 215 410 155 416"/>
    <path class="leader" stroke="var(--y2011)" d="M310 358 C268 350 232 352 227 332"/>
    <path class="leader" stroke="var(--y2012)" d="M376 328 C360 312 372 302 364 293"/>

    <!-- value labels -->
    <text class="pie-label" x="746" y="330">35%</text>
    <text class="pie-label" x="697" y="723">29%</text>
    <text class="pie-label" x="92" y="588">11%</text>
    <text class="pie-label" x="104" y="423">10%</text>
    <text class="pie-label" x="210" y="319">8%</text>
    <text class="pie-label" x="351" y="280">7%</text>
  </svg>

  <h1 class="header-title"><strong>SEO</strong> Deep Dive</h1>
  <p class="header-subtitle">6 Years View</p>
  <div class="brand-name">vantrel</div>

  <ul class="legend">
    <li class="legend-item"><span class="legend-swatch" style="background:var(--y2007)"></span>2007</li>
    <li class="legend-item"><span class="legend-swatch" style="background:var(--y2008)"></span>2008</li>
    <li class="legend-item"><span class="legend-swatch" style="background:var(--y2009)"></span>2009</li>
    <li class="legend-item"><span class="legend-swatch" style="background:var(--y2010)"></span>2010</li>
    <li class="legend-item"><span class="legend-swatch" style="background:var(--y2011)"></span>2011</li>
    <li class="legend-item"><span class="legend-swatch" style="background:var(--y2012)"></span>2012</li>
  </ul>

  <p class="footer-note">All images and data are property of Vantrel Technology SA</p>
</main>
</body>
</html>
```